Plastic Surgeon Stationary Design

I Already have the logo. I Want and a clean, minimalist and elegant project. Please, I prefer Black, White and Gold color but you're free to try another ones. Business card,
Letterhead (A4 and Office), Recipes (Letter Pad) (A5), Envelop, Invoice, Computer Bill, Bill Book, Single A4 page size,
You Have to create at least the same materials I already own. I would like to a file to use in word to print letterheads and letter pad.
What I want that you make more changes are the envelopes that are to colorful and not elegant.
I'll not accept any design without my addresses as you can guide yourself with the models I provide.
Here are the addresses too:
"www.clevandrotavares.example" (website)
(My clinics' address)
"SÃO PAULO
Rua Heitor Lunardi, 1870, Lunardi Corporate, Cj 204
São Paulo - SP
(11) 98432-6120"
"BALNEÁRIO CAMBORIÚ
Rua Benedito Kauer, 418, 7° andar
Edificio Vale Azul
Balneário Camboriú - SC
(047) 9246-3180"
Attention: Letterheads, Recipes, have to contain "CRM/SC 27.583 and CRM/SP 238.416" close to my name (Dr. Clevandro Tavares - Cirurgião Plástico), it is usually placed at the bottom.
Designers, attention!
During the process of creating bear in mind that the details of the logo, as the faces on the sides, are designed to be subtle. Highlight other such details affect the delicacy and elegance of the logo and visual identity.
When you are creating stationery, do not abuse the use of the logo, it should be used once or at most two times in each item.
Remember! Each stationery set must submit 3 models, one with the address "Balneario Camboriu", another with the address of "São Paulo" and the third containing both addresses.
The model letter envelope, folder type bag for letterhead and folder with inner pocket that provided a model did not please me because they are very flashy. Give preference to the use of white or black background.
PLEASE! Seek inspiration in the models contained in this link:
https://www.filecrate.example/sh/kq27pz58wnr4c1v/MbTyLo_QaZ
In this link you can find my PAST Stationary Itens, so it can help you on your work
https://stashbin.example/8RkLQ2vNm3TeHwYz
Reason: Nobody presented anything useful.
Reason: still waiting some designers send their projects
Reason: Still Waiting Some Designs....
Target Market(s)
Mostly females with good economical condition. (Class A and AB)
Industry/Entity Type
Business
Requirements
Must have
- You have to provide 3 models of each paper, one with the address of São Paulo, another with the Balneario Camboriú address, and the third one with both addresses.

```html
<!DOCTYPE html>
<html lang="pt-BR">
<head>
<meta charset="utf-8">
<title>Clevandro Tavares — Stationery Set</title>
<link rel="stylesheet" href="https://fonts.googleapis.com/css2?family=Cormorant+Garamond:wght@400;600&family=Montserrat:wght@400&display=swap">
<style>
  :root{
    --bg:#ebebeb;
    --paper:#f7f7f6;
    --ink:#2c2c2f;
    --gold:#b08a5a;
    --gold-soft:#c9a67a;
    --muted:#8d8d90;
    --body:#555558;
    --serif:'Cormorant Garamond', Georgia, serif;
    --sans:'Montserrat', Arial, sans-serif;
  }
  *{box-sizing:border-box;margin:0;padding:0}
  html,body{width:1200px;height:795px;overflow:hidden;background:var(--bg)}
  body{position:relative;font-family:var(--serif);color:var(--ink)}
  .piece{position:absolute;box-shadow:0 2px 6px rgba(0,0,0,.12)}

  .brand{font-family:var(--serif);font-weight:600;color:var(--gold);white-space:nowrap;line-height:1}
  .tagline{font-family:var(--sans);color:var(--gold-soft);letter-spacing:.35em;text-transform:uppercase;line-height:1}

  /* Letterhead */
  .letterhead{left:270px;top:28px;width:345px;height:488px;background:var(--paper);overflow:hidden}
  .letterhead__topbar{position:absolute;left:0;right:0;top:0;height:8px;background:var(--ink);border-bottom:1px solid var(--gold)}
  .letterhead__tab{position:absolute;left:50%;top:0;transform:translateX(-50%);width:128px;height:46px;background:var(--ink);border-bottom:2px solid var(--gold);display:flex;flex-direction:column;align-items:center;justify-content:center;gap:5px}
  .letterhead__tab .brand{font-size:15px}
  .letterhead__tab .tagline{font-size:4px}
  .letter{position:absolute;left:34px;right:34px;top:70px;font-size:7.2px;line-height:1.45;color:var(--body)}
  .letter__recipient{margin-bottom:12px;font-weight:600;color:var(--ink)}
  .letter p{margin-bottom:7px;text-align:justify}
  .letter__signature{width:70px;height:18px;margin-top:6px;background:linear-gradient(90deg,rgba(44,44,47,.25),rgba(44,44,47,.05))}
  .letterhead__footer{position:absolute;left:0;right:0;bottom:0;height:62px;background:var(--ink);border-top:2px solid var(--gold);padding:9px 18px 0;color:#b9b9bb;font-size:6px;line-height:1.5}
  .footer__cols{display:flex;justify-content:space-between}
  .footer__col--mid{text-align:center}
  .footer__col--right{text-align:right}
  .footer__web{text-align:center;color:var(--gold-soft);margin-top:4px;font-size:6.5px}

  /* Folder */
  .folder{left:690px;top:60px;width:390px;height:505px;background:var(--ink);display:flex;flex-direction:column;align-items:center;padding-top:160px;gap:9px}
  .folder .brand{font-size:30px}
  .folder .tagline{font-size:7px}

  /* Business cards */
  .card{width:175px;height:100px;background:var(--ink)}
  .card--front{left:62px;top:238px;display:flex;flex-direction:column;align-items:center;justify-content:center;gap:6px}
  .card--front .brand{font-size:15px}
  .card--front .tagline{font-size:4px}
  .card--back{left:62px;top:356px;padding-top:12px}
  .card--back .brand{font-size:10px;text-align:center}
  .card__band{margin-top:10px;height:26px;background:var(--gold);display:flex;justify-content:space-between;align-items:center;padding:0 10px;font-size:5px;line-height:1.35;color:var(--ink)}
  .card__web{text-align:center;color:var(--gold-soft);font-size:6px;margin-top:9px}

  /* Envelopes */
  .envelope{width:410px;height:200px;background:var(--paper);overflow:hidden}
  .envelope--front{left:160px;top:560px}
  .envelope__band{position:absolute;left:0;right:0;bottom:0;height:82px;background:var(--ink);border-top:2px solid var(--gold);padding:12px 18px 0;color:#b9b9bb;font-size:6.5px;line-height:1.5}
  .envelope--back{left:650px;top:585px}
  .envelope__flap{position:absolute;left:0;right:0;top:0;height:62px;background:var(--ink)}
</style>
</head>
<body>

  <!-- Letterhead -->
  <section class="piece letterhead">
    <div class="letterhead__topbar"></div>
    <div class="letterhead__tab">
      <span class="brand">Clevandro Tavares</span>
      <span class="tagline">Cirurgia Plástica</span>
    </div>
    <div class="letter">
      <div class="letter__recipient">Mr. Arlen Vance<br>Marketing Director<br>Florianópolis</div>
      <p>Thank you for your visit to our clinic last week. We were pleased to discuss your goals and the care plan we prepared for you.</p>
      <p>Our team will contact you soon to confirm the date of your next consultation and share the guidance you need before the procedure.</p>
      <p>Please feel free to reach us at any time with questions.</p>
      <p>Thank you for the trust in our work and our team.</p>
      <p>Sincerely,</p>
      <div class="letter__signature" role="img" aria-label="Handwritten signature of Arlen Vance"></div>
    </div>
    <footer class="letterhead__footer">
      <div class="footer__cols">
        <div class="footer__col">Rua Benedito Kauer, 418<br>7° andar · Edificio Vale Azul<br>(047) 9246-3180</div>
        <div class="footer__col footer__col--mid">Dr. Clevandro Tavares<br>CRM/SC 27.583<br>CRM/SP 238.416</div>
        <div class="footer__col footer__col--right">Rua Heitor Lunardi, 1870<br>Lunardi Corporate, Cj 204<br>(11) 98432-6120</div>
      </div>
      <div class="footer__web">www.clevandrotavares.example</div>
    </footer>
  </section>

  <!-- Presentation folder -->
  <section class="piece folder">
    <span class="brand">Clevandro Tavares</span>
    <span class="tagline">Cirurgia Plástica</span>
  </section>

  <!-- Business cards -->
  <section class="piece card card--front">
    <span class="brand">Clevandro Tavares</span>
    <span class="tagline">Cirurgia Plástica</span>
  </section>
  <section class="piece card card--back">
    <div class="brand">Clevandro Tavares</div>
    <div class="card__band">
      <span>Rua Benedito Kauer, 418<br>(047) 9246-3180</span>
      <span>Rua Heitor Lunardi, 1870<br>(11) 98432-6120</span>
    </div>
    <div class="card__web">www.clevandrotavares.example</div>
  </section>

  <!-- DL envelope, front -->
  <section class="piece envelope envelope--front">
    <div class="envelope__band">
      <div class="footer__cols">
        <div class="footer__col">Dr. Clevandro Tavares<br>Rua Benedito Kauer, 418, 7° andar<br>Edificio Vale Azul<br>(047) 9246-3180</div>
        <div class="footer__col footer__col--right">Rua Heitor Lunardi, 1870<br>Lunardi Corporate, Cj 204<br>São Paulo - SP<br>(11) 98432-6120</div>
      </div>
      <div class="footer__web">www.clevandrotavares.example</div>
    </div>
  </section>

  <!-- DL envelope, back -->
  <section class="piece envelope envelope--back">
    <div class="envelope__flap"></div>
  </section>

</body>
</html>
```